Education related business need name card design

We need name card design for long term study agent.
Company name is Harbor Lantern.
We support clients to connect to the world.
Clients are Japanese family who has primary and secondary school students.

Company Logo is reflection of the globe and HL (Harbor Lantern).
Since business is related to education, we would like to show reliability and love to see the world map (atlas) in the name card.

Target Market(s)

late 30's to 50's parents of primary and secondary students who are enthusiastic for education. Secondary school management

Industry/Entity Type

Education

Contact Information for Business Card

Company name, Address, Official position, Name, Phone number, +65 9555 0142, ayane.mori@harborlantern.sg,

Font styles to use
Serif
Other font styles liked:
• Century Gothic(logo)

Requirements
Must have
• Since businee is related to education, we would like to show reliability and love to see the world map (atlas) in the name card.

```html
<!DOCTYPE html>
<html lang="en">
<head>
<meta charset="utf-8">
<title>Harbor Lantern – Business Card</title>
<link href="https://fonts.googleapis.com/css2?family=Libre+Baskerville:wght@400;700&family=Lora:wght@400&display=swap" rel="stylesheet">
<style>
  :root {
    --canvas: #e6e6e6;
    --paper: #ffffff;
    --navy: #233f8c;
    --brand-blue: #1f6fbf;
    --map-light: #2f68b8;
    --map-mid: #2a58a6;
    --ink-light: #ffffff;
  }
  * { margin: 0; padding: 0; box-sizing: border-box; }
  html, body {
    width: 1200px; height: 1200px; overflow: hidden;
    background: var(--canvas);
  }
  .card {
    position: absolute; top: 229px;
    width: 468px; height: 724px;
    overflow: hidden;
  }
  .card--front { left: 82px; background: var(--paper); }
  .card--back { left: 633px; background: var(--navy); color: var(--ink-light); }

  .brand-mark {
    position: absolute; left: 0; right: 0; top: 332px;
    display: flex; align-items: center; justify-content: center; gap: 12px;
    color: var(--brand-blue);
    font-family: "Libre Baskerville", serif; font-weight: 700;
    font-size: 24px; letter-spacing: 0.5px;
  }
  .brand-mark__dot {
    width: 24px; height: 24px; border-radius: 50%;
    background: var(--brand-blue);
  }

  .world-map {
    position: absolute; left: 30px; top: 0;
    width: 438px; height: 350px;
    border-radius: 0 0 0 60% / 0 0 0 40%;
    background: radial-gradient(ellipse at 60% 35%, var(--map-light) 0%, var(--map-mid) 55%, var(--navy) 100%);
  }

  .company-name {
    position: absolute; left: 31px; top: 156px;
    font-family: "Libre Baskerville", serif; font-weight: 700;
    font-size: 28px; line-height: 37px; letter-spacing: 1px;
    text-transform: uppercase;
  }
  .contact {
    position: absolute; left: 31px; top: 384px;
    font-family: "Lora", serif;
    font-size: 21px; line-height: 30px; letter-spacing: 0.3px;
  }
  .contact__name, .contact__role {
    font-family: "Libre Baskerville", serif; font-weight: 700;
    font-size: 19px; line-height: 34px; letter-spacing: 0.3px;
    text-transform: uppercase;
  }
  .contact__line { text-transform: uppercase; }
  .contact__web { text-transform: none; }
</style>
</head>
<body>
  <section class="card card--front">
    <div class="brand-mark">
      <span class="brand-mark__dot"></span>
      <span class="brand-mark__name">Harbor Lantern</span>
    </div>
  </section>

  <section class="card card--back">
    <div class="world-map" role="img" aria-label="World map (atlas) in soft blue tones"></div>
    <h1 class="company-name">Harbor<br>Lantern<br>Pte. Ltd.</h1>
    <div class="contact">
      <p class="contact__name">Mori Ayane</p>
      <p class="contact__role">Chief Operating Officer</p>
      <p class="contact__line">Keel Lane 42</p>
      <p class="contact__line">08 Tidewater Point</p>
      <p class="contact__line">Singapore 108842</p>
      <p class="contact__line">T: +65 555 0140</p>
      <p class="contact__line">M: +65 9555 0142</p>
      <p class="contact__line">F: +65 555 0141</p>
      <p class="contact__web">ayane.mori@harborlantern.sg</p>
      <p class="contact__web">www.harborlantern.sg</p>
    </div>
  </section>
</body>
</html>
```